QRVoltana Wendlio Mobile Experience

Design the following Observation and Care Path mobile app pages so they are very modern, cool and engaging.
We would also like to modernize our current splash experience (attached).

Observation and Care Path wireframes:
https://k4mzq2.plorvex.com/#g=1&p=observations__-_categories

DO NOT SUBMIT LOGO REDESIGNS. Submit all screens for the above wireframes. If you can improve the Splash screen this is a bonus. Use the same color scheme and logo.

Competitive sample:
https://apps.trivelstore.com/store/apps/details?id=com.zorquin.iphone

```html
<!DOCTYPE html>
<html lang="en">
<head>
<meta charset="utf-8">
<title>QRVoltana Wendlio Mobile Screens</title>
<link href="https://fonts.googleapis.com/css2?family=Montserrat:wght@400;500;600;700&display=swap" rel="stylesheet">
<style>
:root{
  --bg:#e6e7ea;
  --screen:#ffffff;
  --ink:#2b2f38;
  --muted:#9aa0ab;
  --line:#eef0f3;
  --blue:#2f8ff0;
  --blue-deep:#1f6fe8;
  --green:#3ccf6a;
  --orange:#f5a623;
  --red:#f04848;
  --toggle-off:#e3e6ea;
}
*{box-sizing:border-box;margin:0;padding:0}
html,body{width:1200px;height:750px;overflow:hidden}
body{background:var(--bg);font-family:"Montserrat",sans-serif;color:var(--ink);position:relative}
.screens{position:absolute;left:30px;top:140px;display:flex;gap:25px}
.screen{width:212px;height:460px;background:var(--screen);border-radius:22px;padding:14px 14px 0;position:relative;box-shadow:0 20px 40px rgba(40,50,70,.12)}
.screen.is-blue{background:var(--blue);color:#fff}
.status{display:flex;justify-content:space-between;font-size:6.5px;font-weight:600}
.status .dots{letter-spacing:1px}
.badges{display:flex;justify-content:flex-end;gap:3px;margin-top:4px}
.badge{width:7px;height:7px;border-radius:50%}
.badge.orange{background:var(--orange)}
.badge.green{background:var(--green)}
.back{font-size:10px;margin-top:2px}
.title{font-size:10.5px;font-weight:600;margin-top:4px}
.tabs{display:flex;gap:16px;margin-top:12px;font-size:7.5px;color:var(--muted);border-bottom:1px solid var(--line)}
.is-blue .tabs{color:rgba(255,255,255,.75);border-color:rgba(255,255,255,.2)}
.tab{padding-bottom:6px}
.tab.active{color:var(--ink);font-weight:600;border-bottom:1.5px solid var(--blue-deep)}
.is-blue .tab.active{color:#fff;border-color:#123f9e}
.section-label{font-size:6.5px;font-weight:600;margin-top:12px;color:var(--ink)}
.is-blue .section-label{color:#fff}
.hint{font-size:5.5px;color:var(--muted);text-align:right;margin-top:-8px}
.category-list{list-style:none;margin-top:14px}
.category{display:flex;justify-content:space-between;align-items:center;font-size:8px;font-weight:500;height:31px}
.category svg{width:12px;height:12px;stroke:var(--ink);fill:none;stroke-width:1.2}
.care-list{list-style:none;margin-top:10px}
.care-item{display:flex;gap:9px;align-items:flex-start;height:44px}
.care-num{font-size:12px;color:#c3c8cf;font-weight:600;width:10px;padding-top:6px}
.care-text{flex:1}
.care-name{font-size:7.5px;font-weight:600}
.care-desc{font-size:5.5px;color:var(--muted);margin-top:2px;line-height:1.35}
.toggle{width:20px;height:11px;border-radius:6px;background:var(--toggle-off);position:relative;margin-top:2px}
.toggle::after{content:"";position:absolute;left:1px;top:1px;width:9px;height:9px;border-radius:50%;background:#fff;box-shadow:0 1px 2px rgba(0,0,0,.2)}
.toggle.on{background:var(--green)}
.toggle.on::after{left:10px}
.btn{display:inline-block;font-size:6.5px;font-weight:600;color:#fff;background:var(--blue-deep);border-radius:8px;padding:3px 10px}
.btn.grey{background:#c9ccd2}
.save-row{display:flex;justify-content:space-between;align-items:center;margin-top:4px}
.footnote{font-size:5.5px;color:var(--muted)}
.med-list{list-style:none;margin-top:10px}
.med-item{display:flex;justify-content:space-between;align-items:center;font-size:7px;height:28px;border-bottom:1px solid rgba(255,255,255,.15)}
.med-item .mark{width:8px;font-size:6px}
.med-item .label{flex:1}
.question{font-size:7px;margin-top:10px}
.answers{display:flex;gap:8px;margin-top:10px}
.answer{font-size:6.5px;border:1px solid var(--ink);border-radius:8px;padding:3px 9px}
.plain-list{list-style:none;margin-top:10px}
.plain-list li{display:flex;gap:6px;font-size:7px;height:26px;align-items:center}
.plain-list .mark{color:var(--blue-deep);font-size:6px;width:8px}
.clock-row{display:flex;justify-content:flex-end;gap:6px;margin-top:10px;align-items:center}
.dot-red{width:7px;height:7px;border-radius:50%;background:var(--red)}
.times{font-size:6.5px;font-weight:600;margin-top:8px;line-height:1.6}
.times .confirmed{color:var(--green);font-weight:500;font-size:5.5px}
.tasks{list-style:none;margin-top:8px}
.task{display:flex;align-items:center;gap:12px;height:30px}
.task-code{font-size:14px;font-weight:700;color:#d0d4da;width:30px}
.task-name{font-size:8px;font-weight:600}
.submit-row{display:flex;justify-content:flex-end;margin-top:4px}
.home{position:absolute;bottom:12px;left:50%;width:30px;height:30px;margin-left:-15px;border-radius:50%;border:1px solid var(--line)}
.is-blue .home{border-color:rgba(255,255,255,.35)}
</style>
</head>
<body>
<div class="screens">

  <!-- Observations categories -->
  <section class="screen">
    <div class="status"><span class="dots">●●●●● JL</span><span>9:41 AM</span><span>100%</span></div>
    <div class="badges"><span class="badge orange"></span><span class="badge green"></span></div>
    <div class="back">←</div>
    <h1 class="title">Visit Detail Marlo Penrick</h1>
    <nav class="tabs"><span class="tab">Care Path</span><span class="tab active">Observations</span><span class="tab">Notes</span></nav>
    <ul class="category-list">
      <li class="category">Medication<svg viewBox="0 0 12 12"><rect x="3" y="1" width="6" height="10" rx="3"/><line x1="3" y1="6" x2="9" y2="6"/></svg></li>
      <li class="category">Medical Equipment<svg viewBox="0 0 12 12"><path d="M3 1v5a3 3 0 0 0 6 0"/><circle cx="9" cy="5" r="1"/></svg></li>
      <li class="category">Social<svg viewBox="0 0 12 12"><circle cx="3" cy="6" r="1.5"/><circle cx="9" cy="3" r="1.5"/><circle cx="9" cy="9" r="1.5"/><path d="M4.3 5.3l3.4-1.6M4.3 6.7l3.4 1.6"/></svg></li>
      <li class="category">Environmental<svg viewBox="0 0 12 12"><circle cx="6" cy="6" r="5"/><path d="M1 6h10M6 1c2 2 2 8 0 10M6 1c-2 2-2 8 0 10"/></svg></li>
      <li class="category">Incidents<svg viewBox="0 0 12 12"><path d="M6 1l5 10H1z"/><path d="M6 5v3"/></svg></li>
      <li class="category">Thefts<svg viewBox="0 0 12 12"><rect x="2" y="6" width="8" height="5" rx="1"/><path d="M4 6V4a2 2 0 0 1 4 0"/></svg></li>
      <li class="category">Falls<svg viewBox="0 0 12 12"><path d="M2 2h3v3h3v3h3v3"/></svg></li>
      <li class="category">Change in Condition<svg viewBox="0 0 12 12"><rect x="1.5" y="1.5" width="9" height="9" rx="1"/><path d="M3 7l2-2 2 2 2-3"/></svg></li>
    </ul>
    <span class="home"></span>
  </section>

  <!-- Care Path -->
  <section class="screen">
    <div class="status"><span class="dots">●●●●● JL</span><span>9:41 AM</span><span>100%</span></div>
    <div class="badges"><span class="badge orange"></span><span class="badge green"></span></div>
    <div class="back">←</div>
    <h1 class="title">Visit Detail Marlo Penrick</h1>
    <nav class="tabs"><span class="tab">Careplan</span><span class="tab active">Care Path</span><span class="tab">Observations</span></nav>
    <p class="section-label">CARE PATH</p>
    <p class="hint">(Toggle switch if yes)</p>
    <ul class="care-list">
      <li class="care-item"><span class="care-num">1</span><div class="care-text"><p class="care-name">Tired or Fatigue</p><p class="care-desc">Has the client reported being more tired or fatigue?</p></div><span class="toggle on"></span></li>
      <li class="care-item"><span class="care-num">2</span><div class="care-text"><p class="care-name">Weight gain or swelling</p><p class="care-desc">Has the client reported weight gain or swelling?</p></div><span class="toggle"></span></li>
      <li class="care-item"><span class="care-num">3</span><div class="care-text"><p class="care-name">Discomfort or pain in chest</p><p class="care-desc">Has the client reported discomfort or pain in chest?</p></div><span class="toggle"></span></li>
      <li class="care-item"><span class="care-num">4</span><div class="care-text"><p class="care-name">Increase in caughing</p><p class="care-desc">Has the client reported a new or increase in caughing?</p></div><span class="toggle on"></span></li>
      <li class="care-item"><span class="care-num">5</span><div class="care-text"><p class="care-name">Difficulty in sleeping</p><p class="care-desc">Has the client reported difficulty in sleeping?</p></div><span class="toggle"></span></li>
      <li class="care-item"><span class="care-num">6</span><div class="care-text"><p class="care-name">Issue with the medication</p><p class="care-desc">Is the client reporting issues with their medication?</p></div><span class="toggle on"></span></li>
    </ul>
    <p class="care-name">Prescription required</p>
    <div class="save-row"><span class="footnote">Please check before save.</span><span class="btn">Save</span></div>
    <span class="home"></span>
  </section>

  <!-- Medication, blue -->
  <section class="screen is-blue">
    <div class="status"><span class="dots">●●●●● JL</span><span>9:41 AM</span><span>100%</span></div>
    <div class="badges"><span class="badge" style="background:#444"></span><span class="badge green"></span></div>
    <div class="back">←</div>
    <h1 class="title">Visit Detail Marlo Penrick</h1>
    <nav class="tabs"><span class="tab">Care Path</span><span class="tab active">Observations</span><span class="tab">Notes</span></nav>
    <p class="section-label">Medication</p>
    <ul class="med-list">
      <li class="med-item"><span class="mark">▼</span><span class="label">Patient does not have all their medication(s)</span><span>›</span></li>
      <li class="med-item"><span class="mark">▼</span><span class="label">No refill available from the pharmacy</span><span>›</span></li>
      <li class="med-item"><span class="mark"></span><span class="label">Patient does not have all their medication(s)</span><span>›</span></li>
      <li class="med-item"><span class="mark"></span><span class="label">Patient does not have all their medication(s)</span><span>›</span></li>
      <li class="med-item"><span class="mark"></span><span class="label">Patient does not have all their medication(s)</span><span>›</span></li>
    </ul>
    <span class="home"></span>
  </section>

  <!-- Medication question -->
  <section class="screen">
    <div class="status"><span class="dots">●●●●● JL</span><span>9:41 AM</span><span>100%</span></div>
    <div class="badges"><span class="badge orange"></span><span class="badge green"></span></div>
    <div class="back">←</div>
    <h1 class="title">Visit Detail Marlo Penrick</h1>
    <nav class="tabs"><span class="tab">Care Path</span><span class="tab active">Observations</span><span class="tab">Notes</span></nav>
    <p class="section-label">Medication</p>
    <ul class="plain-list">
      <li><span class="mark">▼</span>Patient does not have all their medication(s)</li>
      <li><span class="mark">▼</span>No refill available from the pharmacy</li>
    </ul>
    <p class="question">Does Patient have enough medication today?</p>
    <div class="answers"><span class="answer">Unsure</span><span class="answer">No</span><span class="answer">Yes</span></div>
    <span class="home"></span>
  </section>

  <!-- Clock In / Out -->
  <section class="screen">
    <div class="status"><span class="dots">●●●●● JL</span><span>9:41 AM</span><span>100%</span></div>
    <div class="badges"><span class="badge orange"></span><span class="badge green"></span></div>
    <div class="back">←</div>
    <h1 class="title">Visit Detail Marlo Penrick</h1>
    <nav class="tabs"><span class="tab active">Clock In/Out</span><span class="tab">Directions</span></nav>
    <div class="clock-row"><span class="btn grey">Clock In</span><span class="btn">Clock Out</span><span class="dot-red"></span></div>
    <p class="times">10/23 at 12:00<br><span class="confirmed">Confirmed - 12:04</span><br>10/23 at 16:00</p>
    <p class="section-label">Plan of care tasks:</p>
    <ul class="tasks">
      <li class="task"><span class="task-code">100</span><span class="task-name">Bathing</span></li>
      <li class="task"><span class="task-code">101</span><span class="task-name">Bathroom Assistance</span></li>
      <li class="task"><span class="task-code">102</span><span class="task-name">Grooming</span></li>
      <li class="task"><span class="task-code">103</span><span class="task-name">Cooking</span></li>
      <li class="task"><span class="task-code">104</span><span class="task-name">Cleaning</span></li>
    </ul>
    <div class="submit-row"><span class="btn">Submit</span></div>
    <p class="footnote">Check your observations</p>
    <span class="home"></span>
  </section>

</div>
</body>
</html>
```